Business card for a shipping supplies business

Needing a business card design. Please see the logo. The logo with the white font should be used if there is a dark background.

We are looking for the following info on the card. Please see the sample info. We will need the info to be changed with a few different employee names and info but all will use the same template.

Business Name: The Crate Heron
Employee Name : Marcus Delaney
Position: Account Manager
Address: 4827 W. Ridge 418 S.
Fort Worth, TX 73948
email: Marcus@thecrateheron.example
telephone: 855-619-2740 x 207
website: www.getparcelkits.example

Target Market(s)

Businesses who ship products for online sales

Industry/Entity Type

Cardboard

Contact Information for Business Card

Name, title, address, website, logo, telephone number

Font styles to use
Sans Serif

Colors
EE7325
F08F49
F5BC92
FAE3D3
FDF4ED

Requirements
Must have
• Logo on back of card. Clean look, just logo, website address

```html
<!DOCTYPE html>
<html lang="en">
<head>
<meta charset="utf-8">
<title>The Crate Heron – Business Card</title>
<link rel="stylesheet" href="https://fonts.googleapis.com/css2?family=Poppins:wght@400;500;600;700&display=swap">
<style>
  :root {
    --page: #2b2e33;
    --card: #141414;
    --white: #ffffff;
    --orange: #ee7325;
    --orange-soft: #f08f49;
    --peach: #f5bc92;
    --text-light: #f2f2f2;
  }
  * { box-sizing: border-box; margin: 0; padding: 0; }
  html, body {
    width: 1200px; height: 1000px; overflow: hidden;
    background: var(--page);
    font-family: "Poppins", sans-serif;
  }
  .canvas {
    position: relative; width: 1200px; height: 1000px;
    display: flex; flex-direction: column; align-items: center; justify-content: center; gap: 36px;
  }
  .card {
    position: relative; width: 770px; height: 440px;
    background: var(--card); border-radius: 22px; overflow: hidden;
    box-shadow: 0 18px 40px rgba(0,0,0,.45);
  }

  /* Brand lockup */
  .brand { display: flex; align-items: center; gap: 16px; }
  .brand-dot { width: 46px; height: 46px; border-radius: 50%; background: var(--orange); flex: none; }
  .brand-name { font-weight: 700; color: var(--white); line-height: 1.05; letter-spacing: .5px; }

  /* Back */
  .card-back .brand { position: absolute; left: 50%; top: 150px; transform: translateX(-50%); }
  .card-back .brand-name { font-size: 46px; white-space: nowrap; }
  .back-web-line {
    position: absolute; left: 0; right: 0; top: 300px;
    display: flex; align-items: center; gap: 26px;
  }
  .back-rule { flex: 1; height: 2px; background: var(--orange); }
  .back-web {
    flex: none; color: var(--text-light); font-size: 20px; letter-spacing: 1.5px; line-height: 1;
  }

  /* Front */
  .card-front .brand { position: absolute; left: 46px; top: 180px; }
  .card-front .brand-name { font-size: 34px; width: 250px; }
  .divider { position: absolute; left: 350px; top: 0; width: 2px; height: 100%; background: var(--orange); }
  .accent-bar { position: absolute; right: 30px; top: 200px; width: 14px; height: 170px; background: var(--orange); }

  .contact { position: absolute; left: 336px; top: 88px; right: 60px; }
  .row { display: flex; align-items: flex-start; gap: 16px; margin-bottom: 10px; }
  .icon {
    width: 30px; height: 30px; border-radius: 50%; background: var(--orange);
    flex: none; display: flex; align-items: center; justify-content: center;
  }
  .icon.person { background: var(--peach); }
  .icon svg { width: 16px; height: 16px; fill: var(--card); }
  .person-name { font-size: 25px; font-weight: 700; color: var(--white); letter-spacing: 1.5px; line-height: 1.1; text-transform: uppercase; }
  .person-title { font-size: 18px; font-weight: 500; color: var(--orange); letter-spacing: 1.5px; text-transform: uppercase; margin-bottom: 18px; }
  .detail { font-size: 17px; color: var(--text-light); letter-spacing: .6px; line-height: 30px; white-space: nowrap; }
</style>
</head>
<body>
<main class="canvas">

  <section class="card card-back" aria-label="Card back">
    <div class="brand">
      <span class="brand-dot"></span>
      <span class="brand-name">The Crate Heron</span>
    </div>
    <div class="back-web-line">
      <span class="back-rule"></span>
      <p class="back-web">www.getparcelkits.example</p>
      <span class="back-rule"></span>
    </div>
  </section>

  <section class="card card-front" aria-label="Card front">
    <div class="brand">
      <span class="brand-dot"></span>
      <span class="brand-name">The Crate Heron</span>
    </div>
    <span class="divider"></span>
    <span class="accent-bar"></span>

    <div class="contact">
      <div class="row">
        <span class="icon person"><svg viewBox="0 0 16 16"><circle cx="8" cy="5" r="3.2"/><path d="M2 15c0-3.5 2.7-5.5 6-5.5s6 2 6 5.5z"/></svg></span>
        <div>
          <p class="person-name">Marcus Delaney</p>
          <p class="person-title">Account Manager</p>
        </div>
      </div>
      <div class="row">
        <span class="icon"><svg viewBox="0 0 16 16"><path d="M3.5 1.5l2.5 0 1 3.5-1.7 1.2a8 8 0 0 0 4.5 4.5L11 9l3.5 1v2.5c0 1-1 2-2 2C6.5 14.5 1.5 9.5 1.5 3.5c0-1 1-2 2-2z"/></svg></span>
        <p class="detail">855-619-2740 x 207</p>
      </div>
      <div class="row">
        <span class="icon"><svg viewBox="0 0 16 16"><path d="M1.5 3.5h13v9h-13z"/><path d="M1.5 3.5l6.5 5 6.5-5" fill="none" stroke="#ee7325" stroke-width="1.2"/></svg></span>
        <p class="detail">Marcus@thecrateheron.example</p>
      </div>
      <div class="row">
        <span class="icon"><svg viewBox="0 0 16 16"><circle cx="8" cy="8" r="6.5" fill="none" stroke="#141414" stroke-width="1.4"/><path d="M1.5 8h13M8 1.5c-3 3.5-3 9.5 0 13M8 1.5c3 3.5 3 9.5 0 13" fill="none" stroke="#141414" stroke-width="1.2"/></svg></span>
        <p class="detail">www.getparcelkits.example</p>
      </div>
      <div class="row">
        <span class="icon"><svg viewBox="0 0 16 16"><path d="M8 1a5 5 0 0 1 5 5c0 3.8-5 9-5 9S3 9.8 3 6a5 5 0 0 1 5-5z"/><circle cx="8" cy="6" r="1.8" fill="#ee7325"/></svg></span>
        <p class="detail">4827 W. Ridge 418 S.<br>Fort Worth, TX 73948</p>
      </div>
    </div>
  </section>

</main>
</body>
</html>
```